Fine Art business needs new website

We need a simple website with a home page, about us page, New sculptures, Sold sculptures, and a contact us page.Our sculptures are very high end one of a kind pieces. As such we need the site to be VERY elegant and professional. Lastly, because I'll be updating pictures on the website on a monthly basis it needs to be user friendly to update (Wordpress is preferred). The only branding we have so far for the business is a business card.
Updates
I wasn't completely ready when this project launched, also I am on the road right now and haven't been able to be as responsive to all you designers as I would like. I will work on giving feedback to all the top designs we've received so far. Thank you all so much for your participation and hardwork.
Target Market(s)
High end customers (affluent), art collectors, interior decorators/designers
Industry/Entity Type
Art Gallery
Coding
Coded - Design and coding required
Number of Pages Required
5+ page
Requirements
Must have
- Easily editable picture gallery for myself so that I can add new pieces(pictures of the pieces), remove sold pieces, etc. I would like the website to be built in wordpress so I can update it. I currently use larkpanelpro through Hostlark for my other business website and would like to do the same for this one.
- Pages:
- -Intro page with featured pieces
- -Current pieces gallery (for sale) mainly a picture gallery
- -Sculptures archive (sold pieces) another picture gallery
- -About us: Pull-down of -about the artist (attached content)
- -Artistic Process (attached content)
- -Show Schedule:
- -one page dedicated to "friends of VMC" (basically a link page)
- TO BE CLEAR "www.pebblecrew.example" IS A TOTALLY DIFFERENT SITE AND I'M NOT TRYING TO COMBINE THE TWO OR JOIN THEM INTO ONE. This page needs be more elegant and seperate from the Pebble Crew site.
- UPDATE: I'd like a link to the VMC Chatterloop page: https://www.chatterloop.example/velmormillco/
Nice to have
- I would like the pictures on the gallery pages able to have text connected with them (Materials, price)
- I would like the site style and fonts to be similar to our business cards we've already had designed (picture attached).
Should not have
- Too much flash or other things that will make the site slow to load.

```html
<!DOCTYPE html>
<html lang="en">
<head>
<meta charset="utf-8">
<title>Velmor Mill Co. — Rocks . Stones . Bones</title>
<link href="https://fonts.googleapis.com/css2?family=Playfair+Display:wght@400;700&family=Cinzel:wght@600;700&family=Open+Sans:wght@400;600;700&display=swap" rel="stylesheet">
<style>
:root{
  --purple:#3d1466;
  --purple-deep:#2a0b47;
  --purple-dark:#1f0836;
  --ink:#222;
  --muted:#777;
  --line:#e3e3e3;
  --card-line:#ececec;
  --white:#fff;
}
*{box-sizing:border-box;margin:0;padding:0}
html,body{width:1200px;height:3084px;overflow:hidden}
body{font-family:"Open Sans",Arial,sans-serif;color:var(--ink);background:var(--white);position:relative}
a{color:inherit;text-decoration:none}

.topbar{height:30px;background:var(--purple);color:#fff;font-size:13px;display:flex;justify-content:flex-end;align-items:center;gap:22px;padding-right:118px}
.topbar span{display:flex;align-items:center;gap:7px}
.topbar .sep{width:1px;height:14px;background:rgba(255,255,255,.6)}

.header{height:122px;display:flex;align-items:center;justify-content:space-between;padding:0 100px}
.brand{display:flex;align-items:center;gap:12px}
.brand-mark{width:28px;height:28px;background:var(--purple)}
.brand-name{font-weight:600;font-size:16px;letter-spacing:2px;color:var(--purple)}
.nav{display:flex;gap:30px;font-size:14px;font-weight:700;color:#333}

.hero{position:relative;height:576px;background:radial-gradient(ellipse at 30% 45%,#b8a7c7 0,#6e5a86 28%,#2c2533 55%,#141014 100%);overflow:hidden}
.hero::after{content:"";position:absolute;inset:0;background:radial-gradient(ellipse at 72% 48%,rgba(190,175,205,.55) 0,rgba(90,70,110,.35) 30%,transparent 55%)}
.hero-text{position:absolute;z-index:2;left:0;right:0;top:214px;text-align:center;color:#fff}
.hero-title{font-family:"Cinzel",serif;font-size:52px;font-weight:700;letter-spacing:3px;text-shadow:0 2px 8px rgba(0,0,0,.5)}
.hero-tag{display:inline-block;margin-top:10px;background:var(--purple);font-family:"Cinzel",serif;font-size:26px;letter-spacing:4px;padding:4px 18px}
.hero-dots{position:absolute;z-index:2;bottom:18px;left:0;right:0;display:flex;justify-content:center;gap:8px}
.hero-dots i{width:12px;height:12px;border-radius:50%;border:2px solid #fff}
.hero-dots i.on{background:#fff}

.about{position:relative;height:472px}
.about-copy{position:absolute;left:100px;top:100px;width:520px}
.section-title{font-family:"Playfair Display",serif;font-weight:700;font-size:31px;color:#222;letter-spacing:1px}
.about-copy p{margin-top:24px;font-size:13px;line-height:22px;color:var(--muted)}
.btn{display:inline-flex;align-items:center;gap:8px;background:var(--purple);color:#fff;font-size:12px;font-weight:700;letter-spacing:1px;padding:12px 18px}
.about-copy .btn{margin-top:34px}
.about-video{position:absolute;left:680px;top:108px;width:420px;height:262px;background:linear-gradient(160deg,#d8d4cf,#8f8a86 55%,#3b3530)}
.play{position:absolute;left:50%;top:50%;width:64px;height:44px;margin:-22px 0 0 -32px;background:#d62020;border-radius:10px;display:flex;align-items:center;justify-content:center}
.divider{position:absolute;left:100px;right:100px;bottom:0;height:1px;background:var(--line)}

.featured{position:relative;height:1552px}
.featured .section-title{position:absolute;top:96px;left:0;right:0;text-align:center}
.card{position:absolute;width:300px;background:#fff;border:1px solid var(--card-line);text-align:center}
.card .photo{height:166px;background:radial-gradient(ellipse at center,#5b4a36 0,#211a15 45%,#0c0a09 80%)}
.card h3{font-size:14px;font-weight:700;margin-top:20px;color:#222}
.card p{font-size:10.5px;line-height:15px;color:var(--muted);margin:8px 20px 0}
.card .price{font-size:22px;font-weight:700;margin:12px 0 18px;color:#222}
.card.raised{box-shadow:0 4px 18px rgba(0,0,0,.15)}
.card.raised .btn{margin:-6px 0 20px;padding:9px 14px;font-size:11px}
.c1{left:100px}.c2{left:450px}.c3{left:800px}
.r1{top:172px}.r2{top:620px}.r3{top:992px}
.view-all{position:absolute;left:474px;top:1368px;width:252px;height:56px;border:2px solid var(--purple);color:var(--purple);font-size:14px;font-weight:700;letter-spacing:1px;display:flex;align-items:center;justify-content:center;gap:10px}

.footer{position:absolute;left:0;top:2752px;width:1200px;height:332px;background:linear-gradient(120deg,var(--purple-deep),var(--purple-dark));color:#fff}
.fcol{position:absolute;top:70px}
.fcol h4{font-size:13px;font-weight:700;letter-spacing:1px}
.fcontact{left:100px}
.fcontact li{list-style:none;display:flex;align-items:center;gap:10px;font-size:12px;margin-top:18px}
.fnews{left:460px}
.field{margin-top:16px;width:300px;height:36px;background:#fff;display:flex;align-items:center;justify-content:space-between;padding:0 12px;color:#666;font-size:12px}
.subscribe{margin-top:12px;display:inline-block;border:1px solid #fff;font-size:12px;font-weight:700;padding:9px 16px;letter-spacing:1px}
.fsocial{left:930px}
.socials{display:flex;gap:10px;margin-top:16px}
.socials i{width:34px;height:34px;border-radius:50%;background:#fff;display:block}
.copyright{position:absolute;left:100px;right:100px;bottom:0;height:80px;border-top:1px solid rgba(255,255,255,.2);display:flex;align-items:center;justify-content:center;font-size:12px}
</style>
</head>
<body>

<div class="topbar">
  <span><svg width="12" height="12" viewBox="0 0 24 24" fill="#fff"><path d="M6.6 10.8a15 15 0 0 0 6.6 6.6l2.2-2.2c.3-.3.7-.4 1-.2 1.1.4 2.3.6 3.6.6.6 0 1 .4 1 1V20c0 .6-.4 1-1 1A17 17 0 0 1 3 4c0-.6.4-1 1-1h3.5c.6 0 1 .4 1 1 0 1.3.2 2.5.6 3.6.1.3 0 .7-.2 1z"/></svg>(555) 210-4418</span>
  <span class="sep"></span>
  <span><svg width="13" height="11" viewBox="0 0 24 18" fill="#fff"><path d="M0 0h24v2L12 10 0 2zM0 4l12 8 12-8v14H0z"/></svg>rowan@pebblecrew.example</span>
</div>

<header class="header">
  <a class="brand" href="#"><span class="brand-mark"></span><span class="brand-name">VELMOR MILL CO.</span></a>
  <nav class="nav"><a href="#">HOME</a><a href="#">ABOUT US</a><a href="#">NEW SCULPTURES</a><a href="#">SOLD SCULPTURES</a><a href="#">CONTACT US</a></nav>
</header>

<section class="hero" role="img" aria-label="Photograph of two halves of a purple amethyst geode on a dark background">
  <div class="hero-text">
    <div class="hero-title">VELMOR MILL CO.</div>
    <div class="hero-tag">ROCKS . STONES . BONES</div>
  </div>
  <div class="hero-dots"><i></i><i class="on"></i><i></i><i></i></div>
</section>

<section class="about">
  <div class="about-copy">
    <h2 class="section-title">ABOUT VELMOR MILL CO.</h2>
    <p>Each piece begins as raw stone gathered from quiet places and shaped by hand over many months. We polish, cut and set every form so its natural color and grain lead the work, never a mold or a copy. Collectors and designers come to us for one of a kind sculpture made to last for generations.</p>
    <a class="btn" href="#">READ MORE <svg width="12" height="12" viewBox="0 0 24 24"><circle cx="12" cy="12" r="11" fill="#fff"/><path d="M10 7l5 5-5 5" stroke="#3d1466" stroke-width="2.5" fill="none"/></svg></a>
  </div>
  <div class="about-video" role="img" aria-label="Video still of the artist working on a white stone sculpture in the studio">
    <div class="play"><svg width="20" height="20" viewBox="0 0 20 20"><path d="M5 3l12 7-12 7z" fill="#fff"/></svg></div>
  </div>
  <div class="divider"></div>
</section>

<section class="featured">
  <h2 class="section-title">FEATURED PIECES</h2>

  <article class="card c1 r1"><div class="photo" role="img" aria-label="Green stone sculpture on a black stand"></div><h3>LOREM IPSUM DOLOR</h3><p>Hand cut stone on a dark base, polished to a soft glow and signed.</p><div class="price">$ 89.00</div></article>
  <article class="card c2 r1 raised"><div class="photo" role="img" aria-label="Gold curved stone sculpture on a black stand"></div><h3>LOREM IPSUM DOLOR</h3><p>Curved golden stone form set on a slim stand, a single studio piece.</p><div class="price">$ 89.00</div><a class="btn" href="#">VIEW DETAILS <svg width="11" height="11" viewBox="0 0 24 24"><circle cx="12" cy="12" r="11" fill="#fff"/><path d="M10 7l5 5-5 5" stroke="#3d1466" stroke-width="2.5" fill="none"/></svg></a></article>
  <article class="card c3 r1"><div class="photo" role="img" aria-label="Purple geode slice sculpture on a stand"></div><h3>LOREM IPSUM DOLOR</h3><p>Amethyst slice in a bronze frame with a raw edge left on display.</p><div class="price">$ 89.00</div></article>

  <article class="card c1 r2"><div class="photo" role="img" aria-label="Amber stone sculpture on a black stand"></div><h3>LOREM IPSUM DOLOR</h3><p>Warm amber stone turned in a slow spiral and mounted on black.</p><div class="price">$ 89.00</div></article>
  <article class="card c2 r2"><div class="photo" role="img" aria-label="Orange twisted stone sculpture"></div><h3>LOREM IPSUM DOLOR</h3><p>Twisted orange stone with deep grain, shaped and finished by hand.</p><div class="price">$ 89.00</div></article>
  <article class="card c3 r2"><div class="photo" role="img" aria-label="Gold open form sculpture on a stand"></div><h3>LOREM IPSUM DOLOR</h3><p>Open gold form carved from one block, shown on a plain dark base.</p><div class="price">$ 89.00</div></article>

  <article class="card c1 r3"><div class="photo" role="img" aria-label="Gold curl stone sculpture"></div><h3>LOREM IPSUM DOLOR</h3><p>Small golden curl of stone, light in hand and bright under light.</p><div class="price">$ 89.00</div></article>
  <article class="card c2 r3"><div class="photo" role="img" aria-label="Blue and purple stone slab on a stand"></div><h3>LOREM IPSUM DOLOR</h3><p>Blue and violet slab framed in metal, edges left in natural shape.</p><div class="price">$ 89.00</div></article>
  <article class="card c3 r3"><div class="photo" role="img" aria-label="Tall green stone sculpture on a stand"></div><h3>LOREM IPSUM DOLOR</h3><p>Tall green column of stone with a fine polish, one of a kind.</p><div class="price">$ 89.00</div></article>

  <a class="view-all" href="#">VIEW ALL PIECES <svg width="14" height="14" viewBox="0 0 24 24"><circle cx="12" cy="12" r="10" fill="none" stroke="#3d1466" stroke-width="2.5"/><path d="M10 7l5 5-5 5" stroke="#3d1466" stroke-width="2.5" fill="none"/></svg></a>
</section>

<footer class="footer">
  <div class="fcol fcontact">
    <h4>CONTACT US</h4>
    <ul>
      <li><svg width="12" height="12" viewBox="0 0 24 24" fill="#fff"><path d="M6.6 10.8a15 15 0 0 0 6.6 6.6l2.2-2.2c.3-.3.7-.4 1-.2 1.1.4 2.3.6 3.6.6.6 0 1 .4 1 1V20c0 .6-.4 1-1 1A17 17 0 0 1 3 4c0-.6.4-1 1-1h3.5c.6 0 1 .4 1 1 0 1.3.2 2.5.6 3.6.1.3 0 .7-.2 1z"/></svg>(555) 210-4418</li>
      <li><svg width="13" height="11" viewBox="0 0 24 18" fill="#fff"><path d="M0 0h24v2L12 10 0 2zM0 4l12 8 12-8v14H0z"/></svg>rowan@pebblecrew.example</li>
    </ul>
  </div>
  <div class="fcol fnews">
    <h4>NEWSLETTER SUBSCRIBE</h4>
    <div class="field">Enter Email<svg width="13" height="11" viewBox="0 0 24 18" fill="#3d1466"><path d="M0 0h24v2L12 10 0 2zM0 4l12 8 12-8v14H0z"/></svg></div>
    <a class="subscribe" href="#">SUBSCRIBE</a>
  </div>
  <div class="fcol fsocial">
    <h4>FOLLOW US ON</h4>
    <div class="socials"><a href="https://www.chatterloop.example/velmormillco/" aria-label="Chatterloop"><i></i></a><i></i><i></i><i></i></div>
  </div>
  <div class="copyright">Copyrights © 2018 Velmor Mill Co. All Rights Reserved.</div>
</footer>

</body>
</html>
```